I need a business card design for my clipvane channel called The Copper Ladle Show. I make clipvane cooking tutorials. I'd like the phrase " I'll see you next time, for my next meal" somewhere on the BC. The Clipvane web address is www.clipvane.example/user/CopperLadleShow
email - advertising@quillreel.example
I have just updated what i am looking for on the card. Thanks
Cooking
The name of my business is The Copper Ladle Show. It's a Clipvane channel & the url is https://www.clipvane.example/user/CopperLadleShow
Am am a ClipVane partner.
My name is Marek.
The Copper Ladle Show
Pictorial/Combination Logo

```html
<!DOCTYPE html>
<html lang="en">
<head>
<meta charset="utf-8">
<title>The Copper Ladle Show – Business Card</title>
<link rel="stylesheet" href="https://fonts.googleapis.com/css2?family=Archivo+Narrow:wght@700&family=Oswald:wght@500&family=Arimo:wght@700&display=swap">
<style>
  :root {
    --backdrop: #8f8f8f;
    --card-dark-edge: #222222;
    --card-dark-mid: #3a3a3a;
    --logo-yellow: #e6e600;
    --gold: #c49a05;
    --paper: #ffffff;
    --ink: #111111;
  }
  * { margin: 0; padding: 0; box-sizing: border-box; }
  html, body { width: 1200px; height: 1200px; overflow: hidden; }
  body {
    position: relative;
    background: var(--backdrop);
    font-family: "Arimo", Arial, sans-serif;
  }
  .card {
    position: absolute;
    left: 190px;
    width: 820px;
    height: 520px;
    overflow: hidden;
  }
  /* Front side */
  .card-front {
    top: 50px;
    background: linear-gradient(90deg, var(--card-dark-edge) 0%, var(--card-dark-mid) 50%, var(--card-dark-edge) 100%);
    display: flex;
    align-items: center;
    justify-content: center;
  }
  .front-wordmark {
    font-family: "Oswald", "Arial Narrow", sans-serif;
    font-weight: 500;
    font-size: 58px;
    letter-spacing: 1px;
    text-transform: uppercase;
    color: var(--logo-yellow);
  }
  /* Back side */
  .card-back {
    top: 630px;
    background: var(--paper);
  }
  .brand-band {
    position: absolute;
    left: 0;
    top: 110px;
    width: 330px;
    height: 323px;
    background: var(--gold);
    display: flex;
    align-items: center;
    justify-content: center;
    padding: 0 24px;
  }
  .band-wordmark {
    font-family: "Oswald", "Arial Narrow", sans-serif;
    font-weight: 500;
    font-size: 40px;
    line-height: 1.15;
    text-align: center;
    text-transform: uppercase;
    color: var(--paper);
  }
  .owner-role {
    position: absolute;
    left: 352px;
    top: 106px;
    writing-mode: vertical-rl;
    transform: rotate(180deg);
    font-family: "Oswald", "Arial Narrow", sans-serif;
    font-weight: 500;
    font-size: 20px;
    color: var(--gold);
    letter-spacing: 1px;
  }
  .owner-name {
    position: absolute;
    left: 392px;
    top: 100px;
    font-family: "Archivo Narrow", "Arial Narrow", sans-serif;
    font-weight: 700;
    font-size: 60px;
    line-height: 1;
    color: var(--ink);
    white-space: nowrap;
  }
  .contact-list {
    position: absolute;
    left: 360px;
    top: 200px;
    list-style: none;
  }
  .contact-item {
    display: flex;
    align-items: center;
    height: 46px;
    font-size: 13px;
    color: var(--ink);
  }
  .contact-icon {
    width: 34px;
    height: 34px;
    margin-right: 12px;
    flex: none;
  }
  .sign-off {
    position: absolute;
    left: 360px;
    right: 30px;
    top: 448px;
    font-family: "Oswald", "Arial Narrow", sans-serif;
    font-weight: 500;
    font-size: 18px;
    letter-spacing: 0.5px;
    color: var(--gold);
    white-space: nowrap;
  }
</style>
</head>
<body>

  <section class="card card-front" aria-label="Card front">
    <p class="front-wordmark">The Copper Ladle Show</p>
  </section>

  <section class="card card-back" aria-label="Card back">
    <div class="brand-band">
      <p class="band-wordmark">The Copper Ladle Show</p>
    </div>

    <p class="owner-role">OWNER</p>
    <h1 class="owner-name">Marek Surname</h1>

    <ul class="contact-list">
      <li class="contact-item">
        <svg class="contact-icon" viewBox="0 0 38 38" aria-hidden="true">
          <circle cx="19" cy="19" r="17" fill="var(--gold)"/>
          <circle cx="19" cy="19" r="12" fill="var(--paper)"/>
          <path d="M14 12.5c1-.8 2-.6 2.6.4l1.2 2.2c.4.8.2 1.5-.5 2l-.8.6c.6 1.6 1.7 2.8 3.3 3.5l.6-.8c.5-.7 1.3-.9 2-.5l2.2 1.2c1 .6 1.1 1.6.4 2.6l-.7.8c-1 1-2.8 1-4.6.1-2.8-1.4-5-3.7-6.3-6.5-.8-1.8-.8-3.6.2-4.6z" fill="var(--gold)"/>
        </svg>
        <span>(12) 555 0147</span>
      </li>
      <li class="contact-item">
        <svg class="contact-icon" viewBox="0 0 38 38" aria-hidden="true">
          <circle cx="19" cy="19" r="17" fill="var(--gold)"/>
          <circle cx="19" cy="19" r="12" fill="var(--paper)"/>
          <rect x="12" y="14" width="14" height="10" rx="1" fill="none" stroke="var(--gold)" stroke-width="1.8"/>
          <path d="M12.5 14.5l6.5 5 6.5-5" fill="none" stroke="var(--gold)" stroke-width="1.8"/>
        </svg>
        <span>advertising@quillreel.example</span>
      </li>
      <li class="contact-item">
        <svg class="contact-icon" viewBox="0 0 38 38" aria-hidden="true">
          <circle cx="19" cy="19" r="17" fill="var(--gold)"/>
          <circle cx="19" cy="19" r="12" fill="var(--paper)"/>
        </svg>
        <span>https://clipvane.example/user/CopperLadleShow</span>
      </li>
      <li class="contact-item">
        <svg class="contact-icon" viewBox="0 0 38 38" aria-hidden="true">
          <circle cx="19" cy="19" r="17" fill="var(--gold)"/>
          <circle cx="19" cy="19" r="12" fill="var(--paper)"/>
        </svg>
        <span>https://friendlane.example/pages/The-Copper-Ladle-Show</span>
      </li>
      <li class="contact-item">
        <svg class="contact-icon" viewBox="0 0 38 38" aria-hidden="true">
          <circle cx="19" cy="19" r="17" fill="var(--gold)"/>
          <circle cx="19" cy="19" r="12" fill="var(--paper)"/>
        </svg>
        <span>https://chirpline.example/Copper-LadleShow</span>
      </li>
    </ul>

    <p class="sign-off">“I'll see you next time, for my next meal”</p>
  </section>

</body>
</html>
```